Brindlequest.com is a mountain biking and climbing travel company. We need a advertisement fo...

We need a advertisement for the back cover of a guide book. We would like a simple but strong ad that includes our logo. It must state that we are a biking and climbing company and people can contact us at the web site brindlequest.com We would like you to incorparate and below photo and logo on the ad.

```html
<!DOCTYPE html>
<html lang="en">
<head>
<meta charset="utf-8">
<title>Brindlequest – Call Us For Booking</title>
<link rel="stylesheet" href="https://fonts.googleapis.com/css2?family=Bebas+Neue&family=Exo+2:wght@600;700&family=Lato:wght@700&display=swap">
<style>
  :root {
    --backdrop: #4d4b4c;
    --orange: #ff6a1f;
    --orange-light: #ff8a45;
    --ink: #0c0c0c;
    --paper: #e6e6e6;
    --white: #ffffff;
    --sky-top: #5d8aa0;
    --sky-mid: #c9b7a0;
    --sky-low: #e08a3c;
    --ground: #3a2c22;
  }
  html, body {
    margin: 0;
    width: 1200px;
    height: 1200px;
    overflow: hidden;
    background: var(--backdrop);
  }
  .flyer {
    position: absolute;
    left: 205px;
    top: 42px;
    width: 789px;
    height: 1116px;
    display: block;
  }
  .headline-light { font-family: "Bebas Neue", sans-serif; fill: var(--paper); }
  .headline-dark { font-family: "Bebas Neue", sans-serif; fill: var(--ink); }
  .phone { font-family: "Exo 2", sans-serif; font-weight: 700; fill: var(--ink); }
  .brand-name { font-family: "Exo 2", sans-serif; font-weight: 600; fill: var(--white); }
  .brand-tagline { font-family: "Exo 2", sans-serif; font-weight: 600; fill: var(--white); letter-spacing: 6px; }
  .web-address { font-family: "Lato", sans-serif; font-weight: 700; fill: var(--ink); }
</style>
</head>
<body>
<svg class="flyer" viewBox="0 0 789 1116" xmlns="http://www.w3.org/2000/svg">
  <defs>
    <linearGradient id="sunsetSky" x1="0" y1="0" x2="0" y2="1">
      <stop offset="0" stop-color="var(--sky-top)"/>
      <stop offset="0.5" stop-color="var(--sky-mid)"/>
      <stop offset="0.75" stop-color="var(--sky-low)"/>
      <stop offset="1" stop-color="var(--ground)"/>
    </linearGradient>
    <linearGradient id="darkHills" x1="0" y1="0" x2="0" y2="1">
      <stop offset="0" stop-color="#111"/>
      <stop offset="1" stop-color="#2a2a2a"/>
    </linearGradient>
    <linearGradient id="bandOrange" x1="0" y1="1" x2="1" y2="0">
      <stop offset="0" stop-color="var(--orange)"/>
      <stop offset="1" stop-color="var(--orange-light)"/>
    </linearGradient>
    <linearGradient id="riderTones" x1="0" y1="0" x2="0" y2="1">
      <stop offset="0" stop-color="#8a7a70"/>
      <stop offset="0.45" stop-color="#6a6a6a"/>
      <stop offset="1" stop-color="#2e2e2e"/>
    </linearGradient>
  </defs>

  <rect class="lower-backdrop" x="0" y="0" width="789" height="1116" fill="url(#darkHills)"/>

  <rect class="hero-photo" x="0" y="0" width="789" height="560" fill="url(#sunsetSky)"
        role="img" aria-label="Photo: woman standing with a mountain bike on a ridge at sunset"/>

  <polygon class="band-black" points="600,484 789,428 789,739 320,902 320,700" fill="var(--ink)"/>
  <polyline class="band-outline" points="320,737 320,902 789,739" fill="none" stroke="var(--white)" stroke-width="2"/>

  <polygon class="band-orange" points="0,539 641,322 644,624 0,852" fill="url(#bandOrange)"/>
  <polygon class="band-phone" points="320,737 789,602 789,689 320,854" fill="url(#bandOrange)"/>

  <polygon class="rider-photo" points="0,852 312,741 312,1116 0,1116" fill="url(#riderTones)"
           role="img" aria-label="Photo: smiling cyclist in a jersey standing beside a mountain bike"/>

  <text class="headline-light" transform="translate(96,612) rotate(-19.6)" font-size="138" textLength="500" lengthAdjust="spacingAndGlyphs">CALL US FOR</text>
  <text class="headline-dark" transform="translate(150,752) rotate(-19.6)" font-size="215" textLength="505" lengthAdjust="spacingAndGlyphs">BOOKING</text>

  <text class="phone" transform="translate(360,796) rotate(-19)" font-size="46" textLength="375" lengthAdjust="spacingAndGlyphs">+41 79 555 0142</text>

  <g class="brand">
    <circle cx="400" cy="966" r="26" fill="none" stroke="var(--white)" stroke-width="4"/>
    <text class="brand-name" x="440" y="980" font-size="38" textLength="300" lengthAdjust="spacingAndGlyphs">BRINDLEQUEST</text>
    <text class="brand-tagline" x="442" y="1003" font-size="12">CLIMBING + RIDING</text>
  </g>

  <rect class="web-box" x="399" y="1030" width="350" height="44" fill="var(--orange)"/>
  <text class="web-address" x="574" y="1060" font-size="23" text-anchor="middle">www.brindlequest.com</text>
</svg>
</body>
</html>
```